Velvane Detailing – Premium Automotive Detailing Studio Website Design

We're launching a premium automotive detailing studio called Velvane Detailing, and we’re looking for a clean, minimal, and high-end website design (desktop + mobile version). The studio targets owners of luxury vehicles who care deeply about aesthetics, perfection, and exceptional service.
This project is about more than just showing services , it should feel like a luxury experience from the very first second. The design should be modern, minimalistic, elegant, and clearly aimed at an upscale market.
We’re looking for a designer who can translate our physical studio’s premium interior and architectural feel into a digital presence.
What we want the website to feel like:
Clean and modern
Professional and luxurious
Minimal and not cluttered
Light animations or transitions to add polish
Stylish and cinematic
Design freedom:
We trust your design direction. We are not providing strict color codes or layout instructions, we want you to create what you believe works best based on our brand positioning and target audience. Just keep it premium, modern, and well-organized.
What the website should include:
Hero section with a bold visual (image or video)
About the Studio — a few blocks explaining our story and focus on quality
Service Overview — clearly showing what we offer (detailing, ceramic coating, interior, etc.)
Gallery/Showcase — show off our work with cars, interior, and the space itself
Client Lounge Area — mention comfort, coffee, and waiting space
Testimonials — social proof from satisfied clients
Location & contact section — map, address, contact form
Footer, simple with nav, contact info, and optional social media
Target audience:
Owners of high-end vehicles (Torvana, Kalvex, etc.)
Car collectors and detailing enthusiasts
People looking for premium-level service and presentation
Brands/creators booking our photo studio

```html
<!DOCTYPE html>
<html lang="en">
<head>
<meta charset="utf-8">
<title>Velvane Detailing – Website Design</title>
<link href="https://fonts.googleapis.com/css2?family=Michroma&family=Libre+Baskerville:wght@700&family=Poppins:wght@400;500;600;700&display=swap" rel="stylesheet">
<style>
:root{
  --red:#e31e24;
  --red-dark:#b8141a;
  --ink:#1c1c1e;
  --ink-2:#2a2a2d;
  --gold:#e0a91c;
  --text:#333;
  --muted:#8a8a8a;
  --line:#e2e2e2;
  --white:#fff;
}
*{margin:0;padding:0;box-sizing:border-box}
html,body{width:1200px;height:3268px;overflow:hidden}
body{position:relative;background:var(--white);font-family:'Poppins',sans-serif;color:var(--text)}
.abs{position:absolute}
.board-band{position:absolute;left:0;top:0;width:1200px;height:377px;background:var(--red)}

/* shared blocks */
.brand{position:absolute;display:flex;align-items:center;gap:5px;color:var(--white);font-family:'Poppins',sans-serif;font-weight:700;letter-spacing:.5px;white-space:nowrap}
.brand i{display:block;background:var(--white)}
.photo{position:absolute}
.heading{position:absolute;left:0;right:0;text-align:center;font-family:'Michroma',sans-serif;color:var(--red);text-transform:uppercase}
.heading::after{content:"";display:block;margin:3px auto 0;width:16px;height:1.5px;background:currentColor}
.heading.on-dark::after{background:var(--white)}
.btn{position:absolute;background:var(--red);color:var(--white);font-weight:600;text-transform:uppercase;text-align:center;white-space:nowrap;border-radius:2px}
.btn.ghost{background:transparent;border:1px solid rgba(255,255,255,.7)}
.slab{position:absolute;left:0;width:100%}
.hero-title{position:absolute;left:0;right:0;text-align:center;font-family:'Libre Baskerville',serif;font-weight:700;color:var(--gold);text-transform:uppercase;line-height:1.2;text-shadow:0 2px 6px rgba(0,0,0,.4)}
.lorem{color:var(--text)}
.field{position:absolute;border:1px solid var(--line);color:#a6a6a6;background:#fff}

/* frames */
.frame{position:absolute;background:var(--white);overflow:hidden}
.preview{left:148px;top:67px;width:652px;height:440px;border:3px solid var(--ink);border-radius:16px}
.desk{left:152px;top:548px;width:646px;height:2287px;border-radius:14px 14px 10px 10px;box-shadow:0 0 0 1px #eee}
.mob{left:859px;top:67px;width:197px;height:3139px;border-radius:14px;box-shadow:0 0 0 1px #ddd}

/* desktop nav */
.nav{position:absolute;left:0;right:0;top:14px;height:20px}
.nav-links{position:absolute;left:258px;top:6px;display:flex;gap:16px;font-size:5.6px;font-weight:500;color:var(--white)}
.nav-links .active{color:var(--red)}

/* service cards */
.svc{position:absolute;background:var(--white);box-shadow:0 2px 8px rgba(0,0,0,.25)}
.svc svg{position:absolute}
.svc h4{position:absolute;color:var(--red);font-weight:600}
.svc p{position:absolute;color:var(--muted);line-height:1.5}

/* testimonial cards */
.quote{position:absolute;background:var(--white)}
.quote .qm{position:absolute;display:flex;gap:2px}
.quote .qm b{display:block;background:var(--red);border-radius:50% 50% 2px 50%}
.quote .stars{position:absolute;color:var(--gold);letter-spacing:1px}
.quote p{position:absolute;color:var(--text);line-height:1.5}
.quote .avatar{position:absolute;border-radius:50%;background:linear-gradient(135deg,#d9c2b2,#8d6b5a);border:1px solid var(--red)}
.quote .who{position:absolute;color:var(--red);font-weight:600;line-height:1.4}
.quote .who small{display:block;color:#b0b0b0;font-weight:400}
.quote .soc{position:absolute;border-radius:50%;background:#2f5fb8}

.footer-links{position:absolute;color:var(--white);line-height:1.9}
.contact-list{position:absolute;color:var(--white);line-height:1.55}
.contact-list li{list-style:none;display:flex;gap:4px;align-items:flex-start}
.contact-list li i{display:block;flex:none;border-radius:50%;background:var(--red);margin-top:2px}
.social{position:absolute;display:flex;gap:6px}
.social i{display:block;background:var(--white);border-radius:2px}
</style>
</head>
<body>

<div class="board-band"></div>

<!-- ===== Top desktop preview ===== -->
<section class="frame preview" aria-label="Desktop hero preview">
  <div class="photo" role="img" aria-label="Detailer kneeling beside a yellow sports car in a dark studio"
       style="left:0;top:0;width:652px;height:340px;background:linear-gradient(100deg,#151517 0%,#26241f 35%,#5d4d18 58%,#b88a12 78%,#d9a414 100%);clip-path:polygon(0 0,100% 0,100% 292px,0 340px)"></div>
  <div class="slab" style="top:288px;height:75px;background:var(--red);clip-path:polygon(0 46px,100% 0,100% 28px,0 75px)"></div>
  <div class="brand" style="left:50px;top:16px;font-size:13px"><i style="width:12px;height:12px"></i>VELVANE<span style="font-size:6px;font-weight:500;letter-spacing:2px;margin-left:2px">DETAILING</span></div>
  <div class="nav-links" style="left:257px;top:25px"><span class="active">HOME</span><span>ABOUT US</span><span>SERVICES</span><span>GALLERY</span><span>CONTACT US</span></div>
  <div class="btn" style="left:504px;top:19px;width:95px;height:17px;line-height:17px;font-size:5.6px">Book An Appointment</div>
  <h1 class="hero-title" style="top:123px;font-size:25px">Best Ever Car<br>Interior Services</h1>
  <div class="btn ghost" style="left:290px;top:204px;width:66px;height:15px;line-height:13px;font-size:5.5px">Our Services</div>
  <h2 style="position:absolute;left:78px;top:412px;font-family:'Michroma',sans-serif;color:var(--red);font-size:15px">ABOUT US</h2>
  <div class="abs" style="left:385px;top:406px;width:170px;height:40px;background:var(--ink);clip-path:polygon(12% 100%,30% 0,70% 0,88% 100%)"></div>
</section>

<!-- ===== Full desktop page ===== -->
<main class="frame desk" aria-label="Desktop homepage">
  <!-- hero -->
  <div class="photo" role="img" aria-label="Detailer kneeling beside a yellow sports car in a dark studio"
       style="left:0;top:0;width:646px;height:340px;background:linear-gradient(100deg,#151517 0%,#26241f 35%,#5d4d18 58%,#b88a12 78%,#d9a414 100%);clip-path:polygon(0 0,100% 0,100% 290px,0 340px)"></div>
  <div class="slab" style="top:285px;height:78px;background:var(--red);clip-path:polygon(0 50px,100% 0,100% 28px,0 78px)"></div>
  <div class="brand" style="left:58px;top:12px;font-size:13px"><i style="width:12px;height:12px"></i>VELVANE<span style="font-size:6px;font-weight:500;letter-spacing:2px;margin-left:2px">DETAILING</span></div>
  <div class="nav-links" style="left:258px;top:21px"><span class="active">HOME</span><span>ABOUT US</span><span>SERVICES</span><span>GALLERY</span><span>CONTACT US</span></div>
  <div class="btn" style="left:495px;top:15px;width:93px;height:16px;line-height:16px;font-size:5.4px">Book An Appointment</div>
  <h1 class="hero-title" style="top:118px;font-size:25px">Best Ever Car<br>Interior Services</h1>
  <div class="btn ghost" style="left:290px;top:195px;width:66px;height:15px;line-height:13px;font-size:5.5px">Our Services</div>

  <!-- about -->
  <h2 style="position:absolute;left:83px;top:400px;font-family:'Michroma',sans-serif;color:var(--red);font-size:15px">ABOUT US</h2>
  <div class="abs" style="left:83px;top:420px;width:18px;height:1.5px;background:var(--red)"></div>
  <p class="abs lorem" style="left:83px;top:434px;width:205px;font-size:5.3px;line-height:1.75">Lorem Ipsum Is Simply Dummy Text Of The Printing And Typesetting Industry. Lorem Ipsum Has Been The Industry's Standard Dummy Text Ever Since The 1500s, When An Unknown Printer Took A Galley Of Type And Scrambled It To Make A Type Specimen Book.<br><br>It Has Survived Not Only Five Centuries, But Also The Leap Into Electronic Typesetting, Remaining Essentially Unchanged.</p>
  <div class="btn" style="left:83px;top:519px;width:54px;height:14px;line-height:14px;font-size:5.5px">Read More</div>
  <div class="abs" style="left:310px;top:468px;width:60px;height:60px;background:#d6d6d6;transform:rotate(45deg)"></div>
  <div class="abs" style="left:304px;top:484px;width:72px;text-align:center;font-family:'Michroma',sans-serif;color:#555;font-size:11px;line-height:1.1">15<br><span style="font-family:'Poppins',sans-serif;font-size:6px;color:#777">YEARS OF<br>EXPERIENCE</span></div>
  <div class="brand" style="left:380px;top:460px;color:var(--ink);font-size:34px;gap:8px"><i style="width:24px;height:24px;background:var(--ink)"></i>VELVANE</div>

  <!-- services -->
  <div class="photo" role="img" aria-label="Dark close-up of a car interior being detailed"
       style="left:0;top:581px;width:646px;height:330px;background:linear-gradient(160deg,#2b2b2e,#141416 60%,#1f1f22);clip-path:polygon(0 30px,100% 0,100% 100%,0 100%)"></div>
  <div class="slab" style="top:874px;height:50px;background:var(--red);clip-path:polygon(0 22px,100% 0,100% 18px,0 50px)"></div>
  <h2 class="heading" style="top:647px;font-size:15px">Our Services</h2>

  <div class="svc" style="left:81px;top:683px;width:110px;height:117px">
    <svg style="left:10px;top:12px" width="26" height="24" viewBox="0 0 26 24" fill="none" stroke="#e31e24" stroke-width="1.4"><rect x="3" y="6" width="20" height="12" rx="2"/><path d="M6 6l2-4h10l2 4M7 18v3M19 18v3"/><circle cx="8" cy="12" r="1.5"/><circle cx="18" cy="12" r="1.5"/></svg>
    <h4 style="left:10px;top:54px;font-size:7.5px">Detailing</h4>
    <p style="left:10px;top:68px;width:92px;font-size:5.3px">Lorem Ipsum is simply dummy text of the printing and typesetting industry.</p>
  </div>
  <div class="svc" style="left:205px;top:683px;width:110px;height:117px">
    <svg style="left:10px;top:12px" width="26" height="24" viewBox="0 0 26 24" fill="none" stroke="#e31e24" stroke-width="1.4"><rect x="8" y="3" width="14" height="18" rx="2"/><path d="M3 8h6M4 12h5M5 16h4"/><circle cx="15" cy="10" r="3"/></svg>
    <h4 style="left:10px;top:54px;font-size:7.5px">Ceramic Coating</h4>
    <p style="left:10px;top:68px;width:92px;font-size:5.3px">Lorem Ipsum is simply dummy text of the printing and typesetting industry.</p>
  </div>
  <div class="svc" style="left:330px;top:683px;width:110px;height:117px">
    <svg style="left:10px;top:12px" width="26" height="24" viewBox="0 0 26 24" fill="none" stroke="#e31e24" stroke-width="1.4"><circle cx="13" cy="4" r="2.5"/><path d="M9 8h8l1 10H8zM6 18h14v3H6z"/></svg>
    <h4 style="left:10px;top:54px;font-size:7.5px">Interior</h4>
    <p style="left:10px;top:68px;width:92px;font-size:5.3px">Lorem Ipsum is simply dummy text of the printing and typesetting industry.</p>
  </div>
  <div class="svc" style="left:454px;top:683px;width:110px;height:117px">
    <svg style="left:10px;top:12px" width="26" height="24" viewBox="0 0 26 24" fill="none" stroke="#e31e24" stroke-width="1.4"><rect x="3" y="10" width="20" height="9" rx="2"/><path d="M6 10l2-4h10l2 4M7 19v3M19 19v3"/><circle cx="13" cy="4" r="2.5"/></svg>
    <h4 style="left:10px;top:54px;font-size:7.5px">Waxing &amp; Sealing</h4>
    <p style="left:10px;top:68px;width:92px;font-size:5.3px">Lorem Ipsum is simply dummy text of the printing and typesetting industry.</p>
  </div>
  <div class="btn" style="left:252px;top:819px;width:44px;height:13px;line-height:13px;font-size:5.3px">View All</div>
  <div class="btn" style="left:303px;top:819px;width:91px;height:13px;line-height:13px;font-size:5.3px">Book An Appointment</div>

  <!-- gallery -->
  <h2 class="heading" style="top:958px;font-size:15px">Our Gallery</h2>
  <div class="photo" role="img" aria-label="Car detail shot" style="left:0;top:1028px;width:50px;height:140px;background:linear-gradient(160deg,#9a9a9e,#3a3a3e)"></div>
  <div class="photo" role="img" aria-label="Silver sports car being washed" style="left:60px;top:1000px;width:139px;height:168px;background:linear-gradient(160deg,#8a8a8e,#d0d0d4 50%,#3c3c40)"></div>
  <div class="photo" role="img" aria-label="Detailer pressure-washing a red sports car" style="left:209px;top:992px;width:235px;height:199px;background:linear-gradient(150deg,#1e2a3a,#4a5568 40%,#b0202a 70%,#7a1118)"></div>
  <div class="photo" role="img" aria-label="Detailer polishing a car with a foam pad" style="left:454px;top:1023px;width:140px;height:145px;background:linear-gradient(160deg,#6b5d52,#c9a66b 40%,#2e2e32)"></div>
  <div class="photo" role="img" aria-label="Car washing bay" style="left:604px;top:1000px;width:42px;height:168px;background:linear-gradient(160deg,#9a9ca2,#3a3c42)"></div>
  <div class="abs" style="left:212px;top:1211px;width:226px;height:1px;background:var(--line)"></div>
  <div class="abs" style="left:322px;top:1208px;width:7px;height:7px;border-radius:50%;background:var(--red)"></div>
  <div class="btn" style="left:252px;top:1232px;width:44px;height:13px;line-height:13px;font-size:5.3px">View All</div>
  <div class="btn" style="left:303px;top:1232px;width:91px;height:13px;line-height:13px;font-size:5.3px">Book An Appointment</div>

  <!-- lounge + testimonials -->
  <div class="slab" style="top:1440px;height:420px;background:var(--ink);clip-path:polygon(0 25px,100% 0,100% 100%,0 100%)"></div>
  <div class="slab" style="top:1828px;height:66px;background:var(--red);clip-path:polygon(0 34px,100% 0,100% 28px,0 66px)"></div>
  <h2 class="heading" style="top:1295px;font-size:15px">Client Lounge Area</h2>
  <div class="abs" style="left:143px;top:1336px;width:359px;height:208px;background:#fff;box-shadow:0 2px 10px rgba(0,0,0,.3)"></div>
  <div class="photo" role="img" aria-label="Client lounge with orange armchairs and a coffee table" style="left:148px;top:1341px;width:349px;height:198px;background:linear-gradient(180deg,#5b6b80 0%,#8e9db0 40%,#c6643a 65%,#6b6f78 100%)"></div>
  <div class="abs" style="left:305px;top:1424px;width:34px;height:34px;border-radius:50%;background:var(--red);border:3px solid #fff"></div>
  <svg class="abs" style="left:317px;top:1434px" width="12" height="14" viewBox="0 0 12 14"><path d="M1 0l11 7-11 7z" fill="#fff"/></svg>

  <h2 class="heading on-dark" style="top:1588px;font-size:15px">Testimonials</h2>

  <div class="quote" style="left:84px;top:1624px;width:150px;height:141px">
    <div class="qm" style="left:10px;top:14px"><b style="width:7px;height:8px"></b><b style="width:7px;height:8px"></b></div>
    <div class="stars" style="left:10px;top:33px;font-size:6px">★★★★★</div>
    <p style="left:10px;top:45px;width:128px;font-size:5.2px">Lorem Ipsum Is Simply Dummy Text Of The Printing And Typesetting Industry. Lorem Ipsum Has Been The Industry's Standard Dummy Text Ever Since The 1500s, When An Unknown Printer Took A Galley...</p>
    <div class="avatar" style="left:10px;top:108px;width:20px;height:20px"></div>
    <div class="who" style="left:36px;top:110px;font-size:5.4px">Mara Quillfeld<small>Lorem Ipsum</small></div>
    <div class="soc" style="left:124px;top:111px;width:14px;height:14px"></div>
  </div>
  <div class="quote" style="left:247px;top:1624px;width:150px;height:141px">
    <div class="qm" style="left:10px;top:14px"><b style="width:7px;height:8px"></b><b style="width:7px;height:8px"></b></div>
    <div class="stars" style="left:10px;top:33px;font-size:6px">★★★★★</div>
    <p style="left:10px;top:45px;width:128px;font-size:5.2px">Lorem Ipsum Is Simply Dummy Text Of The Printing And Typesetting Industry. Lorem Ipsum Has Been The Industry's Standard Dummy Text Ever Since The 1500s, When An Unknown Printer Took A Galley...</p>
    <div class="avatar" style="left:10px;top:108px;width:20px;height:20px"></div>
    <div class="who" style="left:36px;top:110px;font-size:5.4px">Mara Quillfeld<small>Lorem Ipsum</small></div>
    <div class="soc" style="left:124px;top:111px;width:14px;height:14px;background:#1f74b8"></div>
  </div>
  <div class="quote" style="left:411px;top:1624px;width:150px;height:141px">
    <div class="qm" style="left:10px;top:14px"><b style="width:7px;height:8px"></b><b style="width:7px;height:8px"></b></div>
    <div class="stars" style="left:10px;top:33px;font-size:6px">★★★★★</div>
    <p style="left:10px;top:45px;width:128px;font-size:5.2px">Lorem Ipsum Is Simply Dummy Text Of The Printing And Typesetting Industry. Lorem Ipsum Has Been The Industry's Standard Dummy Text Ever Since The 1500s, When An Unknown Printer Took A Galley...</p>
    <div class="avatar" style="left:10px;top:108px;width:20px;height:20px"></div>
    <div class="who" style="left:36px;top:110px;font-size:5.4px">Mara Quillfeld<small>Lorem Ipsum</small></div>
    <div class="soc" style="left:124px;top:111px;width:14px;height:14px"></div>
  </div>
  <div class="btn" style="left:252px;top:1783px;width:44px;height:13px;line-height:13px;font-size:5.3px">View All</div>
  <div class="btn" style="left:303px;top:1783px;width:91px;height:13px;line-height:13px;font-size:5.3px">Book An Appointment</div>

  <!-- inquiry -->
  <h2 class="heading" style="top:1925px;font-size:15px">Quick Inquiry</h2>
  <div class="field" style="left:175px;top:1960px;width:144px;height:17px;font-size:5px;padding:5px 6px">First Name</div>
  <div class="field" style="left:327px;top:1960px;width:144px;height:17px;font-size:5px;padding:5px 6px">Last Name</div>
  <div class="field" style="left:175px;top:1987px;width:144px;height:17px;font-size:5px;padding:5px 6px">Email</div>
  <div class="field" style="left:327px;top:1987px;width:144px;height:17px;font-size:5px;padding:5px 6px">Phone</div>
  <div class="field" style="left:175px;top:2013px;width:296px;height:43px;font-size:5px;padding:5px 6px">How Can We Help?</div>
  <div class="btn" style="left:303px;top:2070px;width:40px;height:14px;line-height:14px;font-size:5.3px">Submit</div>

  <!-- footer -->
  <div class="slab" style="top:2114px;height:160px;background:linear-gradient(160deg,#2c2c2f,#18181a);clip-path:polygon(0 18px,100% 0,100% 100%,0 100%)"></div>
  <div class="brand" style="left:82px;top:2190px;font-size:12px;flex-direction:column;gap:6px"><i style="width:22px;height:22px"></i>VELVANE</div>
  <h3 style="position:absolute;left:204px;top:2160px;font-family:'Michroma',sans-serif;color:var(--red);font-size:7px">CONTACT US</h3>
  <ul class="contact-list" style="left:204px;top:2175px;font-size:5.4px">
    <li><i style="width:5px;height:5px"></i>(555) 014-2281</li>
    <li><i style="width:5px;height:5px"></i>(555) 017-6604</li>
    <li><i style="width:5px;height:5px"></i>info@velvanedetailing.com</li>
    <li><i style="width:5px;height:5px"></i>4820 Harbor Row,<br>Bellmont, LA 70412 USA</li>
  </ul>
  <h3 style="position:absolute;left:316px;top:2160px;font-family:'Michroma',sans-serif;color:var(--red);font-size:7px">QUICK INQUIRY</h3>
  <div class="footer-links" style="left:316px;top:2174px;font-size:5.4px"><span style="color:var(--red)">Home</span><br>About Us<br>Services<br>Gallery<br>Contact Us</div>
  <div class="photo" role="img" aria-label="Map showing the studio location" style="left:428px;top:2158px;width:134px;height:80px;background:linear-gradient(135deg,#7a7358,#a39a7a 45%,#6d6b5e)"></div>
  <div class="slab" style="top:2270px;height:17px;background:var(--red)"></div>
  <p class="abs" style="left:83px;top:2275px;font-size:5.3px;color:#fff">© 2025 Velvane Detailing. All Rights Reserved.</p>
  <div class="social" style="left:520px;top:2274px"><i style="width:7px;height:7px"></i><i style="width:7px;height:7px"></i><i style="width:7px;height:7px;border-radius:50%;background:var(--ink)"></i></div>
</main>

<!-- ===== Mobile page ===== -->
<main class="frame mob" aria-label="Mobile homepage">
  <div class="slab" style="top:0;height:25px;background:var(--red)"></div>
  <p class="abs" style="left:0;right:0;top:8px;text-align:center;color:#fff;font-size:6px;font-weight:600">BOOK AN APPOINTMENT</p>
  <div class="photo" role="img" aria-label="Detailer kneeling beside a yellow sports car in a dark studio"
       style="left:0;top:25px;width:197px;height:375px;background:linear-gradient(110deg,#151517 0%,#2a2720 40%,#6a5716 70%,#b88a12 100%);clip-path:polygon(0 0,100% 0,100% 340px,0 365px)"></div>
  <div class="slab" style="top:358px;height:50px;background:var(--red);clip-path:polygon(0 14px,100% 0,100% 30px,0 50px)"></div>
  <div class="brand" style="left:10px;top:40px;font-size:11px"><i style="width:10px;height:10px"></i>VELVANE</div>
  <div class="abs" style="left:165px;top:40px;width:17px;height:17px;background:var(--red);border-radius:3px"></div>
  <svg class="abs" style="left:169px;top:45px" width="9" height="7" viewBox="0 0 9 7" stroke="#fff" stroke-width="1"><path d="M0 .5h9M0 3.5h9M0 6.5h9"/></svg>
  <h1 class="hero-title" style="top:160px;font-size:19px;line-height:1.35">Best Ever<br>Car Interior<br>Services</h1>
  <div class="btn ghost" style="left:57px;top:250px;width:84px;height:19px;line-height:17px;font-size:6.5px">Our Services</div>

  <h2 style="position:absolute;left:10px;top:443px;font-family:'Michroma',sans-serif;color:var(--red);font-size:12px">ABOUT US</h2>
  <div class="abs" style="left:10px;top:460px;width:28px;height:1.5px;background:var(--ink)"></div>
  <div class="abs" style="left:20px;top:548px;width:44px;height:44px;background:#d6d6d6;transform:rotate(45deg)"></div>
  <div class="abs" style="left:12px;top:556px;width:60px;text-align:center;font-family:'Michroma',sans-serif;color:#555;font-size:10px;line-height:1.1">15<br><span style="font-family:'Poppins',sans-serif;font-size:5px;color:#777">YEARS OF<br>EXPERIENCE</span></div>
  <div class="brand" style="left:62px;top:505px;color:var(--ink);font-size:20px;gap:5px"><i style="width:14px;height:14px;background:var(--ink)"></i>VELVANE</div>
  <p class="abs lorem" style="left:10px;top:624px;width:178px;font-size:6.2px;line-height:1.6">Lorem Ipsum Is Simply Dummy Text Of The Printing And Typesetting Industry. Lorem Ipsum Has Been The Industry's Standard Dummy Text Ever Since The 1500s, When An Unknown Printer Took A Galley Of Type And Scrambled It To Make A Type Specimen Book.<br><br>It Has Survived Not Only Five Centuries, But Also The Leap Into Electronic Typesetting, Remaining Essentially Unchanged.</p>
  <div class="btn" style="left:8px;top:757px;width:74px;height:20px;line-height:20px;font-size:6.5px">Read More</div>

  <div class="photo" role="img" aria-label="Dark close-up of a car interior being detailed"
       style="left:0;top:808px;width:197px;height:690px;background:linear-gradient(170deg,#2b2b2e,#141416 50%,#1f1f22);clip-path:polygon(0 20px,100% 0,100% 100%,0 100%)"></div>
  <div class="slab" style="top:1478px;height:40px;background:var(--red);clip-path:polygon(0 20px,100% 0,100% 14px,0 40px)"></div>
  <h2 class="heading" style="top:858px;font-size:12px;line-height:1.25">Our<br>Services</h2>

  <div class="svc" style="left:8px;top:913px;width:180px;height:104px">
    <svg style="left:12px;top:16px" width="30" height="28" viewBox="0 0 26 24" fill="none" stroke="#e31e24" stroke-width="1.3"><rect x="3" y="6" width="20" height="12" rx="2"/><path d="M6 6l2-4h10l2 4M7 18v3M19 18v3"/><circle cx="8" cy="12" r="1.5"/><circle cx="18" cy="12" r="1.5"/></svg>
    <h4 style="left:12px;top:56px;font-size:9px">Detailing</h4>
    <p style="left:12px;top:71px;width:160px;font-size:6.6px">Lorem Ipsum is simply dummy text of the printing and typesetting industry.</p>
  </div>
  <div class="svc" style="left:8px;top:1032px;width:180px;height:104px">
    <svg style="left:12px;top:16px" width="30" height="28" viewBox="0 0 26 24" fill="none" stroke="#e31e24" stroke-width="1.3"><rect x="8" y="3" width="14" height="18" rx="2"/><path d="M3 8h6M4 12h5M5 16h4"/><circle cx="15" cy="10" r="3"/></svg>
    <h4 style="left:12px;top:56px;font-size:9px">Ceramic Coating</h4>
    <p style="left:12px;top:71px;width:160px;font-size:6.6px">Lorem Ipsum is simply dummy text of the printing and typesetting industry.</p>
  </div>
  <div class="svc" style="left:8px;top:1151px;width:180px;height:104px">
    <svg style="left:12px;top:16px" width="30" height="28" viewBox="0 0 26 24" fill="none" stroke="#e31e24" stroke-width="1.3"><circle cx="13" cy="4" r="2.5"/><path d="M9 8h8l1 10H8zM6 18h14v3H6z"/></svg>
    <h4 style="left:12px;top:56px;font-size:9px">Interior</h4>
    <p style="left:12px;top:71px;width:160px;font-size:6.6px">Lorem Ipsum is simply dummy text of the printing and typesetting industry.</p>
  </div>
  <div class="svc" style="left:8px;top:1270px;width:180px;height:116px">
    <svg style="left:12px;top:16px" width="30" height="28" viewBox="0 0 26 24" fill="none" stroke="#e31e24" stroke-width="1.3"><rect x="3" y="10" width="20" height="9" rx="2"/><path d="M6 10l2-4h10l2 4M7 19v3M19 19v3"/><circle cx="13" cy="4" r="2.5"/></svg>
    <h4 style="left:12px;top:60px;font-size:9px">Waxing &amp; Sealing</h4>
    <p style="left:12px;top:75px;width:160px;font-size:6.6px">Lorem Ipsum is simply dummy text of the printing and typesetting industry.</p>
  </div>
  <div class="btn" style="left:73px;top:1406px;width:52px;height:16px;line-height:16px;font-size:6.5px">View All</div>
  <div class="btn" style="left:36px;top:1431px;width:125px;height:16px;line-height:16px;font-size:6.5px">Book An Appointment</div>

  <h2 class="heading" style="top:1563px;font-size:12px;line-height:1.25">Our<br>Gallery</h2>
  <div class="photo" role="img" aria-label="Car detail shot" style="left:0;top:1620px;width:16px;height:113px;background:linear-gradient(160deg,#9a9a9e,#3a3a3e)"></div>
  <div class="photo" role="img" aria-label="Detailer pressure-washing a red sports car" style="left:21px;top:1611px;width:154px;height:126px;background:linear-gradient(150deg,#1e2a3a,#4a5568 40%,#b0202a 70%,#7a1118)"></div>
  <div class="photo" role="img" aria-label="Detailer polishing a car" style="left:179px;top:1620px;width:18px;height:113px;background:linear-gradient(160deg,#6b5d52,#c9a66b 40%,#2e2e32)"></div>

  <h2 class="heading" style="top:1770px;font-size:12px;line-height:1.25">Client<br>Lounge<br>Area</h2>
  <div class="slab" style="top:1908px;height:420px;background:var(--ink);clip-path:polygon(0 0,100% 0,100% 100%,0 100%)"></div>
  <div class="slab" style="top:2317px;height:45px;background:var(--red);clip-path:polygon(0 18px,100% 0,100% 24px,0 45px)"></div>
  <div class="abs" style="left:4px;top:1836px;width:189px;height:109px;background:#fff;box-shadow:0 2px 8px rgba(0,0,0,.3)"></div>
  <div class="photo" role="img" aria-label="Client lounge with orange armchairs and a coffee table" style="left:8px;top:1840px;width:181px;height:101px;background:linear-gradient(180deg,#5b6b80 0%,#8e9db0 40%,#c6643a 65%,#6b6f78 100%)"></div>
  <div class="abs" style="left:84px;top:1876px;width:28px;height:28px;border-radius:50%;background:var(--red);border:2px solid #fff"></div>
  <svg class="abs" style="left:94px;top:1884px" width="10" height="12" viewBox="0 0 12 14"><path d="M1 0l11 7-11 7z" fill="#fff"/></svg>

  <h2 class="heading on-dark" style="top:1979px;font-size:12px">Testimonials</h2>
  <div class="quote" style="left:8px;top:2017px;width:180px;height:180px">
    <div class="qm" style="left:12px;top:18px"><b style="width:10px;height:12px"></b><b style="width:10px;height:12px"></b></div>
    <div class="stars" style="left:12px;top:44px;font-size:8px">★★★★★</div>
    <p style="left:12px;top:60px;width:158px;font-size:6.6px">Lorem Ipsum Is Simply Dummy Text Of The Printing And Typesetting Industry. Lorem Ipsum Has Been The Industry's Standard Dummy Text Ever Since The 1500s, When An Unknown Printer Took A Galley...</p>
    <div class="avatar" style="left:12px;top:140px;width:24px;height:24px"></div>
    <div class="who" style="left:42px;top:143px;font-size:6.6px">Mara Quillfeld<small>Lorem Ipsum</small></div>
    <div class="soc" style="left:150px;top:143px;width:18px;height:18px"></div>
  </div>
  <div class="abs" style="left:83px;top:2214px;width:6px;height:6px;border-radius:50%;border:1px solid #888"></div>
  <div class="abs" style="left:95px;top:2214px;width:6px;height:6px;border-radius:50%;background:var(--red)"></div>
  <div class="abs" style="left:107px;top:2214px;width:6px;height:6px;border-radius:50%;border:1px solid #888"></div>
  <div class="btn" style="left:73px;top:2238px;width:52px;height:16px;line-height:16px;font-size:6.5px">View All</div>
  <div class="btn" style="left:36px;top:2263px;width:125px;height:16px;line-height:16px;font-size:6.5px">Book An Appointment</div>

  <h2 class="heading" style="top:2396px;font-size:12px">Quick Inquiry</h2>
  <div class="field" style="left:8px;top:2433px;width:180px;height:22px;font-size:6.5px;padding:6px 9px">First Name</div>
  <div class="field" style="left:8px;top:2463px;width:180px;height:22px;font-size:6.5px;padding:6px 9px">Last Name</div>
  <div class="field" style="left:8px;top:2492px;width:180px;height:22px;font-size:6.5px;padding:6px 9px">Phone</div>
  <div class="field" style="left:8px;top:2521px;width:180px;height:22px;font-size:6.5px;padding:6px 9px">Email</div>
  <div class="field" style="left:8px;top:2551px;width:180px;height:52px;font-size:6.5px;padding:6px 9px">How Can We Help?</div>
  <div class="btn" style="left:73px;top:2618px;width:54px;height:18px;line-height:18px;font-size:6.8px">Submit</div>

  <div class="slab" style="top:2664px;height:420px;background:linear-gradient(170deg,#2c2c2f,#18181a);clip-path:polygon(0 10px,100% 0,100% 100%,0 100%)"></div>
  <div class="brand" style="left:0;right:0;top:2703px;font-size:13px;flex-direction:column;gap:8px"><i style="width:30px;height:30px"></i>VELVANE</div>
  <h3 style="position:absolute;left:8px;top:2795px;font-family:'Michroma',sans-serif;color:var(--red);font-size:9px">CONTACT US</h3>
  <ul class="contact-list" style="left:8px;top:2817px;font-size:6.8px">
    <li><i style="width:6px;height:6px"></i>(555) 014-2281</li>
    <li><i style="width:6px;height:6px"></i>(555) 017-6604</li>
    <li><i style="width:6px;height:6px"></i>info@velvanedetailing.com</li>
    <li><i style="width:6px;height:6px"></i>4820 Harbor Row,<br>Bellmont, LA 70412 USA</li>
  </ul>
  <div class="photo" role="img" aria-label="Map showing the studio location" style="left:8px;top:2903px;width:180px;height:82px;background:linear-gradient(135deg,#7a7358,#a39a7a 45%,#6d6b5e)"></div>
  <h3 style="position:absolute;left:8px;top:3001px;font-family:'Michroma',sans-serif;color:var(--red);font-size:9px">QUICK INQUIRY</h3>
  <div class="abs" style="left:8px;top:3021px;width:160px;font-size:7px;color:#fff;line-height:2.2;word-spacing:8px"><span style="color:var(--red)">Home</span> About&nbsp;Us Services<br>Gallery Contact&nbsp;Us</div>
  <div class="slab" style="top:3078px;height:61px;background:var(--red)"></div>
  <div class="social" style="left:66px;top:3088px;gap:10px"><i style="width:9px;height:9px"></i><i style="width:9px;height:9px"></i><i style="width:12px;height:12px;border-radius:50%;background:var(--ink);margin-top:-2px"></i></div>
  <p class="abs" style="left:0;right:0;top:3108px;text-align:center;font-size:6.6px;color:#fff;line-height:1.5">© 2025 Velvane Detailing.<br>All Rights Reserved.</p>
</main>

</body>
</html>
```